Visitenkarten-Design für Immobilienmakler
Zielgruppe
Wir sind ein Immobilienmakler.
Aufgabenstellung
Wicht wäre das es im Druckformat geliefert wird, welches von www.Kravendo.de geliefert wird. Ich habe alle möglichen Logo Varianten angehangen.

```html
<!DOCTYPE html>
<html lang="de">
<head>
<meta charset="utf-8">
<title>Marlow Estate – Visitenkarte</title>
<link rel="stylesheet" href="https://fonts.googleapis.com/css2?family=Montserrat:wght@400;500;600;700&display=swap">
<style>
  :root {
    --bg: #2a2a2c;
    --card-white: #ffffff;
    --brand-orange: #f58524;
    --brand-navy: #1f2a3a;
    --text-dark: #1c1c1c;
    --text-muted: #444444;
    --rule: #2b2b2b;
  }
  * { box-sizing: border-box; margin: 0; padding: 0; }
  html, body {
    width: 1200px; height: 901px; overflow: hidden;
    background: var(--bg);
    font-family: "Montserrat", sans-serif;
  }
  .stage {
    width: 1200px; height: 901px;
    display: flex; align-items: center; justify-content: center; gap: 60px;
  }
  .card {
    position: relative;
    width: 525px; height: 300px;
    box-shadow: 0 12px 30px rgba(0,0,0,.45);
  }
  .card--front { background: var(--card-white); }
  .card--back {
    background: var(--brand-orange);
    display: flex; align-items: center; justify-content: center;
  }
  .brand {
    display: flex; align-items: center; gap: 10px;
    font-weight: 700; letter-spacing: 1px;
  }
  .brand__dot { width: 16px; height: 16px; border-radius: 50%; }
  .card--front .brand {
    position: absolute; left: 38px; top: 64px;
    font-size: 30px; color: var(--brand-navy);
  }
  .card--front .brand__dot { background: var(--brand-orange); }
  .card--back .brand { font-size: 40px; color: var(--card-white); }
  .card--back .brand__dot { background: var(--card-white); width: 20px; height: 20px; }
  .accent-rule {
    position: absolute; left: 230px; right: 40px; top: 170px;
    border-top: 1.5px solid var(--rule);
  }
  .person { position: absolute; left: 38px; top: 186px; }
  .person__name { font-size: 18px; font-weight: 700; color: var(--text-dark); letter-spacing: .3px; }
  .person__role { font-size: 12px; color: var(--text-muted); margin-top: 1px; }
  .contact { list-style: none; margin-top: 12px; }
  .contact__item {
    display: flex; align-items: center; gap: 8px;
    font-size: 12.5px; color: var(--text-dark); line-height: 19px;
  }
  .contact__icon { width: 12px; height: 12px; fill: var(--brand-orange); }
  .website {
    position: absolute; right: 40px; top: 148px;
    font-size: 13px; font-weight: 600; color: var(--text-dark);
  }
  .website__domain { color: var(--brand-orange); }
</style>
</head>
<body>
<main class="stage">
  <section class="card card--front" aria-label="Vorderseite">
    <div class="brand"><span class="brand__dot"></span>Marlow Estate</div>
    <p class="website">www.<span class="website__domain">marlowestate</span>.de</p>
    <div class="accent-rule"></div>
    <div class="person">
      <h1 class="person__name">LENA BRANDT</h1>
      <p class="person__role">Director</p>
      <ul class="contact">
        <li class="contact__item">
          <svg class="contact__icon" viewBox="0 0 24 24" aria-hidden="true"><path d="M6.6 10.8a15.1 15.1 0 0 0 6.6 6.6l2.2-2.2a1 1 0 0 1 1-.25 11.4 11.4 0 0 0 3.6.57 1 1 0 0 1 1 1V20a1 1 0 0 1-1 1A17 17 0 0 1 3 4a1 1 0 0 1 1-1h3.5a1 1 0 0 1 1 1c0 1.25.2 2.45.57 3.57a1 1 0 0 1-.25 1z"/></svg>
          0600 41200-00
        </li>
        <li class="contact__item">
          <svg class="contact__icon" viewBox="0 0 24 24" aria-hidden="true"><path d="M2 5h20v14H2zM4 7v.5l8 5 8-5V7l-8 5z"/></svg>
          kontakt@marlowestate.de
        </li>
      </ul>
    </div>
  </section>
  <section class="card card--back" aria-label="Rückseite">
    <div class="brand"><span class="brand__dot"></span>Marlow Estate</div>
  </section>
</main>
</body>
</html>
```